New Webpage for High Class Expert Witness Services Company

We are looking for a minimalist design for a webpage that just has our logo and an entry form offer to connect with one of our Liaisons.
The entry form should just ask for Name, Email, Contact Info and Description of Project.

Company Name is: The Marlow Crest Advisory Services

Number of Pages Required

1 page

```html
<!DOCTYPE html>
<html lang="en">
<head>
<meta charset="utf-8">
<title>The Marlow Crest Advisory Services — Get in Touch</title>
<link rel="stylesheet" href="https://fonts.googleapis.com/css2?family=Cinzel:wght@400;500&family=Poppins:wght@400;500&display=swap">
<style>
  :root {
    --bg-page: #121212;
    --bg-header: #1b1b1b;
    --field-bg: #1a1a1a;
    --field-border: #3a3a3a;
    --text-main: #f2f2f2;
    --text-soft: #cfcfcf;
    --text-placeholder: #8a8a8a;
    --logo-silver: #c9c9c9;
    --rule: #4a4a4a;
    --btn-bg: #ffffff;
    --btn-text: #141414;
  }
  * { box-sizing: border-box; margin: 0; padding: 0; }
  html, body { width: 1200px; height: 1074px; overflow: hidden; }
  body {
    position: relative;
    background: var(--bg-page);
    font-family: "Poppins", sans-serif;
    color: var(--text-main);
  }
  .backdrop {
    position: absolute; inset: 0;
    background:
      radial-gradient(ellipse 260px 220px at 40px 760px, rgba(255,255,255,0.07), transparent 70%),
      radial-gradient(ellipse 320px 260px at 1140px 420px, rgba(255,255,255,0.05), transparent 70%),
      radial-gradient(ellipse 500px 200px at 300px 520px, rgba(255,255,255,0.025), transparent 70%);
  }
  .site-header {
    position: absolute; left: 0; top: 0; width: 1200px; height: 238px;
    background: var(--bg-header);
    display: flex; align-items: center; justify-content: center; gap: 14px;
  }
  .brand-mark { width: 16px; height: 16px; background: var(--logo-silver); }
  .brand-name {
    font-family: "Cinzel", serif; font-weight: 500;
    font-size: 34px; letter-spacing: 1px; color: var(--logo-silver);
  }
  .contact {
    position: absolute; left: 247px; top: 300px; width: 706px;
  }
  .contact-title {
    font-family: "Cinzel", serif; font-weight: 400;
    font-size: 37px; text-align: center; line-height: 1;
    letter-spacing: 0.5px;
  }
  .contact-intro {
    margin: 16px auto 0; width: 660px;
    font-size: 13px; line-height: 23px; text-align: center; color: var(--text-soft);
  }
  .field { margin-top: 28px; }
  .field:first-of-type { margin-top: 25px; }
  .field-label { display: block; font-size: 12.5px; margin-left: 2px; height: 16px; line-height: 16px; }
  .field-box {
    position: relative; margin-top: 7px; height: 42px;
    background: var(--field-bg); border: 1px solid var(--field-border); border-radius: 5px;
  }
  .field-box.is-multiline { height: 85px; }
  .field-input {
    position: absolute; left: 16px; top: 0; right: 50px; height: 40px;
    background: none; border: none; outline: none;
    font-family: "Poppins", sans-serif; font-size: 13px; color: var(--text-main);
  }
  .field-input::placeholder { color: var(--text-placeholder); }
  textarea.field-input { top: 10px; height: 64px; resize: none; }
  .field-icon { position: absolute; right: 16px; top: 11px; width: 18px; height: 18px; }
  .submit {
    position: absolute; left: 230px; top: 569px; width: 247px; height: 47px;
    background: var(--btn-bg); border: none; border-radius: 24px;
    display: flex; align-items: center; padding-left: 28px;
    font-family: "Poppins", sans-serif; font-weight: 500; font-size: 12.5px; color: var(--btn-text);
  }
  .submit-arrow {
    position: absolute; right: 7px; top: 7px; width: 33px; height: 33px; border-radius: 50%;
    background: linear-gradient(135deg, #e6e6e6, #8d8d8d);
    display: flex; align-items: center; justify-content: center;
  }
  .footer-rule { position: absolute; left: 141px; top: 1000px; width: 918px; height: 1px; background: var(--rule); }
  .footer-note { position: absolute; left: 0; top: 1026px; width: 1200px; text-align: center; font-size: 13px; }
</style>
</head>
<body>
  <div class="backdrop" role="img" aria-label="Faint flowing line pattern in dark grey tones"></div>

  <header class="site-header">
    <span class="brand-mark"></span>
    <span class="brand-name">Marlow Crest Advisory Services</span>
  </header>

  <main class="contact">
    <h1 class="contact-title">GET IN TOUCH</h1>
    <p class="contact-intro">Lorem ipsum dolor sit amet, consectetuer adipiscing elit. Aenean commodo ligula eget dolor. Aenean massa. Cum sociis natoque penatibus et magnis dis parturient montes</p>

    <form>
      <div class="field">
        <label class="field-label" for="name">Your Name</label>
        <div class="field-box">
          <input class="field-input" id="name" type="text" placeholder="Enter your name">
          <svg class="field-icon" viewBox="0 0 24 24" fill="none" stroke="#fff" stroke-width="1.6"><circle cx="12" cy="8" r="4.5"/><path d="M3.5 22c0-4.7 3.8-8 8.5-8s8.5 3.3 8.5 8"/></svg>
        </div>
      </div>
      <div class="field">
        <label class="field-label" for="email">Your Email</label>
        <div class="field-box">
          <input class="field-input" id="email" type="email" placeholder="Enter your Email">
          <svg class="field-icon" viewBox="0 0 24 24" fill="none" stroke="#fff" stroke-width="1.6"><rect x="2" y="5" width="20" height="14" rx="1.5"/><path d="M2.5 5.5l9.5 8 9.5-8M2.5 18.5l7-6.5M21.5 18.5l-7-6.5"/></svg>
        </div>
      </div>
      <div class="field">
        <label class="field-label" for="phone">Your Contact</label>
        <div class="field-box">
          <input class="field-input" id="phone" type="tel" placeholder="Enter your Contact">
          <svg class="field-icon" viewBox="0 0 24 24" fill="none" stroke="#fff" stroke-width="1.6"><path d="M6.5 2.5l3 3.5-2 2.5c1.2 3 3.6 5.4 6.6 6.6l2.5-2 3.5 3-2 3.4C11 19.5 4.5 13 3 5z"/><path d="M14 2.5a8 8 0 0 1 7.5 7.5M14 6a4.5 4.5 0 0 1 4 4"/></svg>
        </div>
      </div>
      <div class="field">
        <label class="field-label" for="project">Description of Project</label>
        <div class="field-box is-multiline">
          <textarea class="field-input" id="project" placeholder="Enter here..."></textarea>
          <svg class="field-icon" viewBox="0 0 24 24" fill="none" stroke="#fff" stroke-width="1.6"><path d="M12 2.5a9.5 9.5 0 1 1-4.6 17.8L2.5 21.5l1.3-4.6A9.5 9.5 0 0 1 12 2.5z"/><circle cx="8" cy="12" r="0.6" fill="#fff"/><circle cx="12" cy="12" r="0.6" fill="#fff"/><circle cx="16" cy="12" r="0.6" fill="#fff"/></svg>
        </div>
      </div>
      <button class="submit" type="submit">CONNECT WITH A LIAISON
        <span class="submit-arrow"><svg width="14" height="14" viewBox="0 0 14 14" fill="none" stroke="#111" stroke-width="1.8"><path d="M2 12L12 2M4.5 2H12v7.5"/></svg></span>
      </button>
    </form>
  </main>

  <div class="footer-rule"></div>
  <footer class="footer-note">© 2026 the marlow crest advisory services all right</footer>
</body>
</html>
```